BrightArc Orthodontics appointment card design

I need appointment cards/ business cards made. Front will be Logo, name, title, email, phone number and location (5327 Varden Hollow Blvd, Ste 412, Concord, NC 28027) . the back should have an appointment card (name, time, date) and also 3 addresses listed with a check box so we can check to which location they are going.
Wendell Pratt Orthodontics
- 6315 Elmore Street, Ste 514, Harrisburg, NC 28075
- 3761 Tessaly Drive NE, Ste 118, Concord, NC 28025
- 2194 Quarrow Medical Drive, Ste 605, Charlotte, NC 28277
Business card can be horizontal or vertical in Design.
I need to be able to edit it to update and add new employees

Requirements
Must have
• Front:
• - Logo
• - Name & Title (able to be edited)
• - phone (704-555-0148) & Email (need to be able to edit)
• - Address: 5327 Varden Hollow Blvd, Ste 412
• Concord, NC 28027
• Back:
• Appointment Card design:
• - Name, time, Date
• - 3 locations w/ a check box so the patient knows where to go:
• Wendell Pratt Orthodontics
• - 6315 Elmore Street, Ste 514, Harrisburg, NC 28075
• - 3761 Tessaly Drive NE, Ste 118, Concord, NC 28025
• - 2194 Quarrow Medical Drive, Ste 605, Charlotte, NC 28277

```html
<!DOCTYPE html>
<html lang="en">
<head>
<meta charset="utf-8">
<title>BrightArc Orthodontics – Cards</title>
<link href="https://fonts.googleapis.com/css2?family=Open+Sans:wght@400;600;700;800&display=swap" rel="stylesheet">
<style>
  :root {
    --brand-blue: #0d76c0;
    --ink: #1f1f1f;
    --paper: #ffffff;
    --backdrop: #2b2b2b;
    --rule: #333333;
  }
  * { box-sizing: border-box; margin: 0; padding: 0; }
  html, body { width: 1200px; height: 895px; overflow: hidden; }
  body {
    background: var(--backdrop);
    font-family: "Open Sans", Arial, sans-serif;
    color: var(--ink);
    position: relative;
  }
  .card {
    position: absolute;
    left: 250px;
    width: 700px;
    height: 400px;
    background: var(--paper);
    overflow: hidden;
  }
  .card--appointment { top: 30px; }
  .card--contact { top: 465px; }

  .wordmark {
    position: absolute;
    display: flex;
    align-items: center;
    gap: 10px;
    color: var(--brand-blue);
    font-weight: 800;
    font-size: 30px;
    line-height: 1;
    letter-spacing: -0.3px;
    white-space: nowrap;
  }
  .wordmark__dot {
    width: 16px; height: 16px;
    border-radius: 50%;
    background: var(--brand-blue);
    flex: none;
  }
  .card--appointment .wordmark { top: 42px; right: 56px; }
  .card--contact .wordmark { top: 150px; left: 52px; }

  .appt-fields {
    position: absolute;
    left: 52px; right: 56px;
    top: 122px;
    font-size: 15px;
  }
  .appt-fields__row { display: flex; align-items: flex-end; gap: 6px; height: 34px; }
  .appt-fields__label { white-space: nowrap; }
  .appt-fields__line { flex: 1; border-bottom: 1.5px dotted var(--rule); margin-bottom: 4px; }

  .practice-band {
    position: absolute;
    left: 0; right: 0;
    top: 205px;
    height: 38px;
    background: var(--brand-blue);
    color: #fff;
    font-weight: 700;
    font-size: 16px;
    letter-spacing: 0.4px;
    text-transform: uppercase;
    display: flex;
    align-items: center;
    padding-left: 240px;
  }

  .locations {
    position: absolute;
    left: 58px;
    top: 262px;
    list-style: none;
    font-size: 15.5px;
  }
  .locations__item { display: flex; align-items: center; gap: 14px; height: 34px; }
  .locations__box { width: 15px; height: 15px; border: 1.5px solid var(--ink); flex: none; }

  .person {
    position: absolute;
    top: 40px; right: 56px;
    text-align: right;
  }
  .person__name {
    color: var(--brand-blue);
    font-weight: 800;
    font-size: 40px;
    line-height: 1.05;
    white-space: nowrap;
  }
  .person__title { font-size: 17px; }

  .office-address {
    position: absolute;
    right: 56px;
    top: 225px;
    text-align: right;
    font-size: 19px;
    line-height: 1.35;
    font-style: normal;
  }

  .contact-list {
    position: absolute;
    left: 52px;
    bottom: 38px;
    list-style: none;
    font-size: 19px;
  }
  .contact-list__item { display: flex; align-items: center; gap: 12px; height: 30px; }
  .contact-list__icon { width: 16px; height: 16px; flex: none; fill: var(--brand-blue); }
</style>
</head>
<body>

<section class="card card--appointment" aria-label="Appointment card">
  <div class="wordmark"><span class="wordmark__dot"></span>BrightArc Orthodontics</div>

  <div class="appt-fields">
    <div class="appt-fields__row">
      <span class="appt-fields__label">Name:</span><span class="appt-fields__line"></span>
      <span class="appt-fields__label">Date:</span><span class="appt-fields__line"></span>
    </div>
    <div class="appt-fields__row">
      <span class="appt-fields__label">Time:</span><span class="appt-fields__line"></span>
    </div>
  </div>

  <div class="practice-band">Wendell Pratt Orthodontics</div>

  <ul class="locations">
    <li class="locations__item"><span class="locations__box"></span>6315 Elmore Street, Ste 514, Harrisburg, NC 28075</li>
    <li class="locations__item"><span class="locations__box"></span>3761 Tessaly Drive NE, Ste 118, Concord, NC 28025</li>
    <li class="locations__item"><span class="locations__box"></span>2194 Quarrow Medical Drive, Ste 605, Charlotte, NC 28277</li>
  </ul>
</section>

<section class="card card--contact" aria-label="Business card">
  <div class="person">
    <div class="person__name">Marlo Tennant</div>
    <div class="person__title">Director</div>
  </div>

  <div class="wordmark"><span class="wordmark__dot"></span>BrightArc Orthodontics</div>

  <address class="office-address">
    5327 Varden Hollow Blvd, Ste 412<br>
    Concord, NC 28027
  </address>

  <ul class="contact-list">
    <li class="contact-list__item">
      <svg class="contact-list__icon" viewBox="0 0 16 16" aria-hidden="true"><path d="M3.6 1.2l2.2 2.6-1.3 1.6c.9 2 2.3 3.4 4.3 4.3l1.6-1.3 2.6 2.2-1.4 2.3C7 12.6 3.4 9 2.1 2.6z"/></svg>
      704-555-0148
    </li>
    <li class="contact-list__item">
      <svg class="contact-list__icon" viewBox="0 0 16 16" aria-hidden="true"><path d="M1 3.5h14v9H1z M1.5 4l6.5 5 6.5-5" stroke="#fff" stroke-width="1.2"/></svg>
      info@brightarcortho.com
    </li>
    <li class="contact-list__item">
      <svg class="contact-list__icon" viewBox="0 0 16 16" aria-hidden="true"><circle cx="8" cy="8" r="7"/><path d="M1 8h14M8 1c-3 3.5-3 10.5 0 14M8 1c3 3.5 3 10.5 0 14" stroke="#fff" stroke-width="1" fill="none"/></svg>
      www.brightarcortho.com
    </li>
  </ul>
</section>

</body>
</html>
```